Keystone Home Sales website

i need a website that is to get customers to let us sell their house within 30 days with no sales fees based in the uk. iv uploaded a design i like for the website i own i want a copy of this but for the different logo ect need the house buying logo i own to be changed to Keystone Home Sales
it needs to be able to flash up to sell your house today contact box to collect their details such as property type, address, number of bedrooms, (estate agents valuation) , best price you can accept after they have seen the main section banner with advertising why use us.
the three reasons in the banner to use us needs to be
1: We will sell your house in 30 days and ensure we take a buyers fee for our service from the buyer meaning your buyer is secured unlike with most estate agents
2: We do not charge you any fees at all! our small fee is charged to the buyer
3: A huge network of investors and private buyers connecting many estate agents, auction houses, investors, and private buyers to ensure a fast sale.

```html
<!DOCTYPE html>
<html lang="en">
<head>
<meta charset="utf-8">
<title>Keystone Home Sales</title>
<link href="https://fonts.googleapis.com/css2?family=Poppins:wght@300;400;500;600;700&display=swap" rel="stylesheet">
<style>
:root{
  --blue:#1b92d1;
  --blue-dark:#1577ab;
  --ink:#333537;
  --muted:#6d6f72;
  --line:#c9cbce;
  --white:#ffffff;
  --sky-top:#9fc3da;
  --sky-low:#c7e0ee;
  --grass:#6fa33b;
  --grass-dark:#3f6b21;
  --page:#f4f5f6;
  --card:#ffffff;
  --footer:#38393b;
  --skyline:#8d8d92;
  --backdrop:rgba(22,26,30,.46);
}
*{box-sizing:border-box;margin:0;padding:0}
html,body{width:704px;height:1200px;overflow:hidden}
body{font-family:"Poppins",sans-serif;background:var(--page);color:var(--ink);position:relative}
.abs{position:absolute}

/* header + hero */
.hero{left:0;top:0;width:704px;height:484px;background:linear-gradient(var(--sky-top),var(--sky-low) 55%,var(--grass) 82%,var(--grass-dark));}
.hero-art{left:0;top:180px;width:704px;height:304px;background:linear-gradient(rgba(230,180,130,0),rgba(210,160,110,.35) 40%,rgba(90,140,60,.6));}
.follow{left:114px;top:27px;display:flex;align-items:center;gap:5px;font-size:7px;font-weight:600;color:#2d3a44}
.social-box{width:14px;height:14px;border-radius:2px;background:var(--blue)}
.brand-top{left:252px;top:12px;width:200px;text-align:center}
.brand-mark{width:18px;height:18px;border-radius:3px;background:var(--blue);margin:0 auto 4px}
.brand-name{font-weight:400;color:var(--blue);font-size:9px}
.btn-login{left:492px;top:23px;width:42px;height:20px;background:#3b3d40;color:#fff;font-size:6.5px;font-weight:500;border-radius:2px;display:flex;align-items:center;justify-content:center}
.btn-register{left:539px;top:23px;width:50px;height:20px;background:var(--blue);color:#fff;font-size:6.5px;font-weight:500;border-radius:2px;display:flex;align-items:center;justify-content:center}
.search-card{left:114px;top:154px;width:475px;height:82px;background:#fff;border-radius:6px;border-bottom:2px solid var(--blue)}
.search-field{left:12px;top:22px;width:120px;height:20px;border:1px solid var(--line);border-radius:3px;font-size:6px;color:var(--muted);padding:3px 5px}
.search-btn{right:12px;top:24px;width:90px;height:18px;background:var(--blue);color:#fff;font-size:6.5px;font-weight:600;border-radius:2px;display:flex;align-items:center;justify-content:center}

/* why choose us */
.why-title{left:0;top:518px;width:704px;text-align:center;font-size:24px;color:var(--blue);font-weight:400}
.why-title b{color:var(--ink);font-weight:600}
.why-sub{left:0;top:552px;width:704px;text-align:center;font-size:8px;color:var(--ink)}
.divider{left:352px;top:574px;width:1px;height:26px;background:#bbb}
.reason{width:147px;background:var(--card);border-radius:6px;border-bottom:2px solid var(--ink);text-align:center;padding:32px 14px 0}
.reason-icon{left:49px;top:-25px;width:50px;height:50px;border-radius:50%;background:var(--ink);display:flex;align-items:center;justify-content:center}
.reason.featured{border-bottom-color:var(--blue)}
.reason.featured .reason-icon{background:var(--blue)}
.reason h3{font-size:12px;font-weight:600;line-height:14.5px;color:var(--ink)}
.reason.featured h3{color:var(--blue)}
.reason p{font-size:6.8px;font-weight:300;line-height:12.2px;color:var(--muted);margin-top:6px}

/* skyline + footer */
.skyline{left:0;top:797px;width:704px;height:190px;background:linear-gradient(rgba(141,141,146,0),var(--skyline) 45%,var(--footer));}
.footer{left:0;top:980px;width:704px;height:220px;background:var(--footer)}
.foot-mark{left:336px;top:34px;width:32px;height:32px;border-radius:5px;background:var(--blue)}
.foot-name{left:0;top:86px;width:704px;text-align:center;color:var(--blue);font-size:18px;font-weight:400}
.foot-social{left:311px;top:113px;display:flex;gap:5px}
.foot-social .social-box{width:17px;height:17px}
.foot-rule{left:114px;width:475px;height:1px;background:#505154}
.foot-nav{left:114px;top:157px;width:475px;display:flex;justify-content:space-between;color:#d2d3d5;font-size:8px}
.copyright{left:0;top:194px;width:704px;text-align:center;color:#c8c9cb;font-size:8px}

/* modal */
.backdrop{left:0;top:0;width:704px;height:1200px;background:var(--backdrop)}
.modal{left:152px;top:87px;width:400px;height:393px;background:#fff;border-radius:8px;border-bottom:3px solid var(--blue)}
.modal-close{left:536px;top:80px;width:24px;height:24px;border-radius:50%;background:var(--blue)}
.modal-brand{left:0;top:29px;width:400px;text-align:center}
.modal-brand .brand-mark{width:20px;height:20px}
.modal-title{left:20px;top:78px;width:360px;text-align:center;font-size:17px;line-height:23px;font-weight:400;color:var(--ink)}
.modal-title strong{color:var(--blue);font-weight:600}
.field{left:29px;width:342px;height:27px;border:1px solid var(--line);border-radius:3px}
.field label{position:absolute;left:6px;top:-7px;background:#fff;padding:0 3px;font-size:8px;color:var(--muted)}
.field .placeholder{position:absolute;left:9px;top:8px;font-size:7.4px;color:#7a7c80}
.field svg{position:absolute;right:10px;top:11px}
.submit{left:29px;top:342px;width:342px;height:27px;background:var(--blue);color:#fff;font-size:9.5px;font-weight:700;border-radius:3px;display:flex;align-items:center;justify-content:center}
</style>
</head>
<body>

<header class="abs hero">
  <div class="abs hero-art" role="img" aria-label="Illustrated street of detached houses with trees and two homeowners saying they want to sell their house"></div>
  <div class="abs follow"><span>FOLLOW:</span><i class="social-box"></i><i class="social-box"></i><i class="social-box"></i><i class="social-box"></i></div>
  <div class="abs brand-top"><div class="brand-mark"></div><div class="brand-name">Keystone Home Sales</div></div>
  <div class="abs btn-login">LOG IN</div>
  <div class="abs btn-register">REGISTER</div>
  <div class="abs search-card">
    <div class="abs search-field">Property Type</div>
    <div class="abs search-btn">Sell Now</div>
  </div>
</header>

<section>
  <h2 class="abs why-title">Why <b>Choose</b> Us</h2>
  <p class="abs why-sub">The U.K's Leading Company In Selling Houses With 0% Fees.</p>
  <div class="abs divider"></div>

  <article class="abs reason" style="left:114px;top:609px;height:148px">
    <div class="abs reason-icon"><svg width="26" height="22" viewBox="0 0 26 22" fill="none" stroke="#fff" stroke-width="1.4"><path d="M2 11 10 3l8 8M4 9v11h12V9"/><circle cx="20" cy="13" r="5"/><path d="M20 10v3l2 1"/></svg></div>
    <h3>We'll Sell Your<br>House In 30 Days</h3>
    <p>We will sell your house in 30 days and ensure we take a buyers fee for our service from the buyer meaning your buyer is secured unlike with most estate agents</p>
  </article>

  <article class="abs reason featured" style="left:278px;top:636px;height:120px">
    <div class="abs reason-icon"><svg width="30" height="30" viewBox="0 0 30 30" fill="none" stroke="#fff" stroke-width="1.4"><circle cx="15" cy="15" r="12"/><rect x="4" y="11" width="22" height="8" rx="1.5"/></svg></div>
    <h3>We Do Not Charge<br>Any Fees</h3>
    <p>We do not charge you any fees at all! our small fee is charged to the buyer.</p>
  </article>

  <article class="abs reason" style="left:442px;top:609px;height:148px">
    <div class="abs reason-icon"><svg width="28" height="28" viewBox="0 0 28 28" fill="none" stroke="#fff" stroke-width="1.3"><circle cx="14" cy="14" r="4"/><circle cx="14" cy="3" r="2"/><circle cx="14" cy="25" r="2"/><circle cx="3" cy="14" r="2"/><circle cx="25" cy="14" r="2"/><circle cx="6" cy="6" r="2"/><circle cx="22" cy="22" r="2"/><circle cx="22" cy="6" r="2"/><circle cx="6" cy="22" r="2"/><path d="M14 5v5M14 18v5M5 14h5M18 14h5M7.5 7.5l3.5 3.5M17 17l3.5 3.5M20.5 7.5 17 11M11 17l-3.5 3.5"/></svg></div>
    <h3>A Huge Network<br>Of Investors</h3>
    <p>A huge network of investors and private buyers connecting many estate agents, auction houses, investors, and private buyers to ensure a fast sale.</p>
  </article>
</section>

<div class="abs skyline" role="img" aria-label="Silhouette of the London skyline with observation wheel, towers and bridge"></div>

<footer class="abs footer">
  <div class="abs foot-mark"></div>
  <div class="abs foot-name">Keystone Home Sales</div>
  <div class="abs foot-social"><i class="social-box"></i><i class="social-box"></i><i class="social-box"></i><i class="social-box"></i></div>
  <div class="abs foot-rule" style="top:148px"></div>
  <nav class="abs foot-nav"><span>HOME</span><span>|</span><span>ABOUT</span><span>|</span><span>FAQ'S</span><span>|</span><span>SELL</span><span>|</span><span>BLOGS</span><span>|</span><span>CONTACT</span></nav>
  <div class="abs foot-rule" style="top:182px"></div>
  <p class="abs copyright">Copyright © 2023. Keystone Home Sales. All Right Reserved.</p>
</footer>

<div class="abs backdrop"></div>

<div class="abs modal" role="dialog" aria-label="Sell your house today">
  <div class="abs modal-brand"><div class="brand-mark"></div><div class="brand-name">Keystone Home Sales</div></div>
  <h2 class="abs modal-title">Wait! <strong>We Can Help You To Sell Your Property Today,</strong> Please Fill In Your Details</h2>

  <div class="abs field" style="top:138px"><label>Property Type</label><span class="placeholder">Enter Your Property Type</span><svg width="7" height="5" viewBox="0 0 7 5"><path d="M0 0h7L3.5 5z" fill="#5d5f62"/></svg></div>
  <div class="abs field" style="top:179px"><label>Location</label><span class="placeholder">Enter Your Location</span><svg width="7" height="5" viewBox="0 0 7 5"><path d="M0 0h7L3.5 5z" fill="#5d5f62"/></svg></div>
  <div class="abs field" style="top:220px"><label>Bedrooms</label><span class="placeholder">Enter Number Of Bedrooms</span><svg width="7" height="5" viewBox="0 0 7 5"><path d="M0 0h7L3.5 5z" fill="#5d5f62"/></svg></div>
  <div class="abs field" style="top:261px"><label>Valuation</label><span class="placeholder">Enter Your Property Valuation</span><svg width="7" height="5" viewBox="0 0 7 5"><path d="M0 0h7L3.5 5z" fill="#5d5f62"/></svg></div>
  <div class="abs field" style="top:302px"><label>Best Price</label><span class="placeholder">Enter The Best Price You Can Accept</span></div>

  <div class="abs submit">Sell My House Now</div>
</div>
<div class="abs modal-close"><svg width="24" height="24" viewBox="0 0 24 24" stroke="#fff" stroke-width="1.5"><path d="M8 8l8 8M16 8l-8 8"/></svg></div>

</body>
</html>
```